Designer and consultant for professionals/businesses and manufacturers in the kitchen and bath in...

I have 30 years of design experience, and 19 of those years within the marketing team of a national cabinet manufacturer. This role gave me the opportunity to consult and design for kitchen/bath businesses, from boutique to multi-store national scale. My services include layout and spatial planning, individual display design, and product design for cabinet manufacturers. From showrooms, to trade shows to integrated design collections. I would like to see designs that convey professionalism, as well as an appeal to the creative designer mind!

Target Market(s)

Kitchen and bath dealers, as well as mid-scale multi-store home centers. Cabinet manufacturers, Trade Show agencies.

Industry/Entity Type

Kitchen

Contact Information for Business Card

Serving Kitchen and Bath Businesses

Logo Text

MT (initials for business name)

Font styles to use
Serif
Sans Serif
Decorative

Colors
e34197

Requirements
Must have
• Marlowe Tavish Design and Consulting, Inc. (business name)
• marlowe@mtvantra.com (email)
• 917-555-0148 (phone)
• mtvantra.com (website)
Nice to have
• Inclusions of geometric shapes; particularly a 30/15 degree triangle and circle(s)
• 2 colors
Should not have
• Not too artsy!

```html
<!DOCTYPE html>
<html lang="en">
<head>
<meta charset="utf-8">
<title>Marlowe Tavish Design and Consulting, Inc. — Business Cards</title>
<link rel="stylesheet" href="https://fonts.googleapis.com/css2?family=Montserrat:wght@300;400;500;600&display=swap">
<style>
  :root {
    --backdrop: #d4d4d4;
    --charcoal: #3f4042;
    --blush: #f7c5c4;
    --paper: #ffffff;
    --ink: #3a3a3c;
  }
  * { box-sizing: border-box; margin: 0; padding: 0; }
  html, body { width: 1200px; height: 900px; overflow: hidden; }
  body {
    background: var(--backdrop);
    font-family: "Montserrat", Arial, sans-serif;
    display: flex; flex-direction: column; align-items: center; justify-content: center;
    gap: 48px;
  }
  .card {
    position: relative; width: 640px; height: 366px; overflow: hidden;
    box-shadow: 0 3px 8px rgba(0,0,0,.25);
  }
  .card__shapes { position: absolute; inset: 0; }

  /* Front */
  .card--front { background: var(--charcoal); }
  .monogram {
    position: absolute; display: flex; align-items: center; gap: 12px;
    font-weight: 400; letter-spacing: 2px;
  }
  .card--front .monogram { left: 430px; top: 112px; color: var(--paper); font-size: 84px; }
  .monogram__circle {
    width: 22px; height: 22px; border-radius: 50%; border: 2px solid currentColor;
  }
  .brand { position: absolute; }
  .card--front .brand { left: 40px; bottom: 42px; }
  .brand__name { font-size: 36px; line-height: 1.05; font-weight: 400; }
  .brand__first { color: var(--blush); font-weight: 600; }
  .card--front .brand__last { color: var(--paper); }
  .brand__tagline { font-size: 17px; font-weight: 300; letter-spacing: .5px; margin-top: 4px; }
  .card--front .brand__tagline { color: var(--paper); padding-left: 4px; }

  /* Back */
  .card--back { background: var(--paper); }
  .card--back .monogram { right: 150px; top: 32px; color: var(--blush); font-size: 64px; }
  .card--back .brand { right: 40px; top: 122px; text-align: right; }
  .card--back .brand__name { font-size: 30px; }
  .card--back .brand__last { color: var(--ink); }
  .card--back .brand__tagline { color: var(--ink); font-size: 15px; }
  .contact {
    position: absolute; right: 40px; top: 210px; display: flex; gap: 18px;
    font-size: 13px; color: var(--ink);
  }
  .contact__item { display: flex; align-items: center; gap: 6px; }
  .contact__icon { width: 14px; height: 14px; }
  .service {
    position: absolute; left: 30px; top: 80px; width: 180px; text-align: center;
    color: var(--blush); font-size: 21px; line-height: 1.25; font-weight: 400;
  }
  .website {
    position: absolute; left: 36px; bottom: 28px; font-size: 13px; color: var(--ink);
  }
  .website strong { font-weight: 600; }
</style>
</head>
<body>

<section class="card card--front" aria-label="Business card front">
  <svg class="card__shapes" viewBox="0 0 640 366" aria-hidden="true">
    <polygon points="455,0 640,0 640,366 565,366" fill="var(--blush)"/>
  </svg>
  <div class="monogram"><span class="monogram__circle"></span><span>MT</span></div>
  <div class="brand">
    <p class="brand__name"><span class="brand__first">Marlowe</span><span class="brand__last">Tavish</span></p>
    <p class="brand__tagline">Design &amp; Consulting, Inc.</p>
  </div>
</section>

<section class="card card--back" aria-label="Business card back">
  <svg class="card__shapes" viewBox="0 0 640 366" aria-hidden="true">
    <polygon points="0,0 200,0 245,250 0,268" fill="var(--charcoal)"/>
    <polygon points="0,280 470,250 400,366 0,366" fill="var(--blush)"/>
  </svg>
  <p class="service">Serving<br>Kitchen &amp; Bath<br>Business</p>
  <div class="monogram"><span class="monogram__circle"></span><span>MT</span></div>
  <div class="brand">
    <p class="brand__name"><span class="brand__first">Marlowe</span><span class="brand__last">Tavish</span></p>
    <p class="brand__tagline">Design &amp; Consulting, Inc.</p>
  </div>
  <div class="contact">
    <span class="contact__item">
      <svg class="contact__icon" viewBox="0 0 14 14" aria-hidden="true">
        <circle cx="7" cy="7" r="7" fill="var(--blush)"/>
        <path d="M4.5 4h1.6l.6 1.6-.9.7a4.5 4.5 0 0 0 2 2l.7-.9 1.6.6V9.6c0 .4-.4.7-.8.7A5.8 5.8 0 0 1 3.8 4.8c0-.4.3-.8.7-.8z" fill="var(--paper)"/>
      </svg>917-555-0148</span>
    <span class="contact__item">
      <svg class="contact__icon" viewBox="0 0 14 14" aria-hidden="true">
        <circle cx="7" cy="7" r="7" fill="var(--blush)"/>
        <rect x="3.5" y="4.5" width="7" height="5" fill="none" stroke="var(--paper)" stroke-width="1"/>
        <path d="M3.5 4.5 7 7.3l3.5-2.8" fill="none" stroke="var(--paper)" stroke-width="1"/>
      </svg>marlowe@mtvantra.com</span>
  </div>
  <p class="website">www.<strong>mtvantra</strong>.com</p>
</section>

</body>
</html>
```